Healthcare Recruitment Agency Brochure

We need our current Brochure updated as its old and dated. The brochure will be for our current and potential Clients and should provide all the necessary information regarding our services, but in a well presented, easy reading format which echoes our company Brand. The company supplies Healthcare establishments with trained healthcare Staff which can be in a variety of settings.
UPDATE: Following the submission of many designs we would like to amend the information/content to be included in the brochure and have uploaded additional information. We would like an 8 page booklet with the various sections spread out so as not to look to 'wordy' page 1 Front cover, 2 About Us, 3 Our Service, 4 Our promise, 5 Our Staff, 6 Our Ethos, 7 What Our Clients Say/Testimonials, 8 Contact Us/Back page. Please if using pictures (which is welcomed) steer away from the surgical/doctor type. We mainly provide care to the Elderly within Nursing and Residential Homes and Support Environments. Thanks
Updates

Target Market(s)

Healthcare clientell

Industry/Entity Type

Healthcare

Requirements
Must have
• Pictures, animation, easy reading, informative, tie in with website theme www.carewellstaffline.example
Nice to have
• open to ideas
Should not have
• very long text paragraphs

```html
<!DOCTYPE html>
<html lang="en">
<head>
<meta charset="utf-8">
<title>Carewell Staffline – Our Staff Brochure Spread</title>
<link rel="stylesheet" href="https://fonts.googleapis.com/css2?family=Montserrat:ital,wght@0,400;0,500;0,600;0,700;0,800;1,500;1,600;1,700;1,800&display=swap">
<style>
  :root {
    --teal: #17b08c;
    --teal-text: #25b39b;
    --cyan: #33bfc1;
    --blue: #1d4fa6;
    --blue-deep: #173f96;
    --blue-text: #2a50a2;
    --paper: #f6f7f8;
    --backdrop: #8c8c8c;
  }
  * { box-sizing: border-box; margin: 0; padding: 0; }
  html, body { width: 1200px; height: 1200px; overflow: hidden; }
  body {
    background: var(--backdrop);
    font-family: "Montserrat", sans-serif;
    display: flex; align-items: center; justify-content: center;
  }
  .spread {
    width: 1140px; height: 820px;
    display: flex;
    box-shadow: 0 18px 40px rgba(0,0,0,.3);
  }
  .panel {
    position: relative;
    width: 380px; height: 820px;
    background: var(--paper);
    overflow: hidden;
  }
  .panel + .panel { border-left: 1px solid rgba(0,0,0,.06); }
  .panel-art { position: absolute; inset: 0; width: 100%; height: 100%; }
  .panel-content { position: absolute; inset: 0; }

  /* Left panel */
  .accommodating-intro {
    position: absolute; left: 0; top: 0; width: 380px; height: 118px;
    padding: 24px 26px 0;
    color: #fff; font-weight: 800; font-style: italic; text-transform: uppercase;
    font-size: 12.5px; line-height: 1.55; letter-spacing: .3px;
  }
  .promise-list { position: absolute; left: 22px; right: 22px; top: 138px; list-style: none; }
  .promise-list li {
    display: flex; gap: 9px;
    font-style: italic; font-weight: 600; font-size: 12.5px; line-height: 1.35;
    margin-bottom: 15px;
  }
  .promise-list li.blue { color: var(--blue-text); }
  .promise-list li.teal { color: var(--teal-text); }
  .feedback-band {
    position: absolute; left: 0; bottom: 0; width: 380px; height: 92px;
    padding: 20px 22px 0; display: flex; gap: 9px;
    color: #fff; font-style: italic; font-weight: 600; font-size: 12.5px; line-height: 1.35;
  }

  .bullet { flex: 0 0 auto; width: 18px; height: 18px; margin-top: 1px; }

  /* Middle panel */
  .section-title {
    position: absolute; top: 30px; left: 0; width: 380px; text-align: center;
    color: #fff; font-weight: 800; font-size: 38px; letter-spacing: 5px;
  }
  .section-title svg { display: block; margin: 2px auto 0; }
  .vetting-intro {
    position: absolute; top: 166px; left: 30px; right: 26px;
    color: var(--blue-text); font-weight: 800; text-transform: uppercase;
    font-size: 13px; line-height: 1.5;
  }
  .vetting-list { position: absolute; top: 255px; left: 28px; right: 22px; list-style: none; }
  .vetting-list li {
    display: flex; gap: 11px;
    font-weight: 500; font-size: 18px; line-height: 1.22; margin-bottom: 11px;
  }
  .vetting-list li .bullet { width: 21px; height: 21px; margin-top: 1px; }
  .vetting-list li.teal { color: var(--teal-text); }
  .vetting-list li.blue { color: var(--blue-text); }
  .vetting-list li.small { font-size: 14px; line-height: 1.35; }

  /* Right panel */
  .checks-list { position: absolute; top: 112px; left: 26px; right: 24px; list-style: none; }
  .checks-list li {
    display: flex; gap: 11px;
    font-weight: 500; font-size: 16.5px; line-height: 1.3; margin-bottom: 20px;
  }
  .checks-list li .bullet { width: 22px; height: 22px; }
  .checks-list li.teal { color: var(--teal-text); }
  .checks-list li.blue { color: var(--blue-text); }
  .training-copy {
    position: absolute; top: 380px; left: 30px; right: 28px;
    color: var(--blue-text); font-weight: 600; font-size: 17px; line-height: 1.45;
    text-align: center;
  }
  .training-copy p + p { margin-top: 22px; }
</style>
</head>
<body>
<main class="spread">

  <section class="panel panel-promise">
    <svg class="panel-art" viewBox="0 0 380 820" preserveAspectRatio="none" aria-hidden="true">
      <defs>
        <linearGradient id="promiseFoot" x1="0" y1="0" x2="1" y2="0">
          <stop offset="0" stop-color="#1a4aa3"/><stop offset="1" stop-color="#1f5cb3"/>
        </linearGradient>
      </defs>
      <rect x="0" y="0" width="380" height="118" fill="#17a887"/>
      <rect x="0" y="728" width="380" height="92" fill="url(#promiseFoot)"/>
    </svg>
    <div class="panel-content">
      <p class="accommodating-intro">We know that our clients often have a lot on their plate, which is why we pride ourselves on being extremely accommodating:</p>
      <ul class="promise-list">
        <li class="teal"><svg class="bullet" viewBox="0 0 20 20"><circle cx="10" cy="10" r="8.5" fill="none" stroke="currentColor" stroke-width="2"/><path d="M7.5 6.5 L14 10 L7.5 13.5Z" fill="currentColor"/></svg><span>We can visit you at a time to suit you, to discuss your requirements and our service.</span></li>
        <li class="blue"><svg class="bullet" viewBox="0 0 20 20"><circle cx="10" cy="10" r="8.5" fill="none" stroke="currentColor" stroke-width="2"/><path d="M7.5 6.5 L14 10 L7.5 13.5Z" fill="currentColor"/></svg><span>We will give you our client application pack including everything you need to know, to start booking staff from Carewell Staffline we simply need a completed client account form.</span></li>
        <li class="teal"><svg class="bullet" viewBox="0 0 20 20"><circle cx="10" cy="10" r="8.5" fill="none" stroke="currentColor" stroke-width="2"/><path d="M7.5 6.5 L14 10 L7.5 13.5Z" fill="currentColor"/></svg><span>We have staff available to work at the drop of a hat – we understand the need for urgency and will make it our mission to try to help you every time.</span></li>
        <li class="blue"><svg class="bullet" viewBox="0 0 20 20"><circle cx="10" cy="10" r="8.5" fill="none" stroke="currentColor" stroke-width="2"/><path d="M7.5 6.5 L14 10 L7.5 13.5Z" fill="currentColor"/></svg><span>Our friendly office staff will always be at the end of the phone to deal with your requests – we never outsource to call centres.</span></li>
        <li class="blue"><svg class="bullet" viewBox="0 0 20 20"><circle cx="10" cy="10" r="8.5" fill="none" stroke="currentColor" stroke-width="2"/><path d="M7.5 6.5 L14 10 L7.5 13.5Z" fill="currentColor"/></svg><span>We will never leave you waiting and always be honest and realistic in telling you whether we can help.</span></li>
        <li class="teal"><svg class="bullet" viewBox="0 0 20 20"><circle cx="10" cy="10" r="8.5" fill="none" stroke="currentColor" stroke-width="2"/><path d="M7.5 6.5 L14 10 L7.5 13.5Z" fill="currentColor"/></svg><span>When you have booked a staff member you will always receive their compliance form, in a format that suits you.</span></li>
        <li class="blue"><svg class="bullet" viewBox="0 0 20 20"><circle cx="10" cy="10" r="8.5" fill="none" stroke="currentColor" stroke-width="2"/><path d="M7.5 6.5 L14 10 L7.5 13.5Z" fill="currentColor"/></svg><span>You can choose how frequently and in which format we send you your staff rotas, we will be completely flexible to your needs.</span></li>
        <li class="blue"><svg class="bullet" viewBox="0 0 20 20"><circle cx="10" cy="10" r="8.5" fill="none" stroke="currentColor" stroke-width="2"/><path d="M7.5 6.5 L14 10 L7.5 13.5Z" fill="currentColor"/></svg><span>We are always interested in how we could improve; we will regularly review our service and come and visit you when requested.</span></li>
      </ul>
      <div class="feedback-band"><svg class="bullet" viewBox="0 0 20 20"><circle cx="10" cy="10" r="8.5" fill="none" stroke="#fff" stroke-width="2"/><path d="M7.5 6.5 L14 10 L7.5 13.5Z" fill="#fff"/></svg><span>We will regularly send you monitoring forms so you can quickly and easily pass on your feedback about the staff members we are sending you.</span></div>
    </div>
  </section>

  <section class="panel panel-staff">
    <svg class="panel-art" viewBox="0 0 380 820" preserveAspectRatio="none" aria-hidden="true">
      <defs>
        <linearGradient id="staffTop" x1="0" y1="0" x2="1" y2="1">
          <stop offset="0" stop-color="#1fb394"/><stop offset=".45" stop-color="#33bfc1"/><stop offset="1" stop-color="#1d55b0"/>
        </linearGradient>
        <linearGradient id="staffFoot" x1="0" y1="0" x2="1" y2="1">
          <stop offset="0" stop-color="#1d55b0"/><stop offset=".5" stop-color="#33bfc1"/><stop offset="1" stop-color="#17a887"/>
        </linearGradient>
      </defs>
      <rect x="0" y="0" width="380" height="200" fill="url(#staffTop)"/>
      <rect x="0" y="700" width="380" height="120" fill="url(#staffFoot)"/>
      <polygon points="0,70 190,150 380,70 380,778 190,730 0,778" fill="#f6f7f8"/>
    </svg>
    <div class="panel-content">
      <h2 class="section-title">OUR STAFF
        <svg width="220" height="18" viewBox="0 0 220 18" aria-hidden="true"><polyline points="0,10 95,10 102,2 110,16 117,6 122,10 220,10" fill="none" stroke="#fff" stroke-width="2"/></svg>
      </h2>
      <p class="vetting-intro">All our candidates go through a thorough vetting and recruitment process and only ever commence assignments after the following:</p>
      <ul class="vetting-list">
        <li class="teal"><svg class="bullet" viewBox="0 0 20 20"><circle cx="10" cy="10" r="8.5" fill="none" stroke="currentColor" stroke-width="2"/><path d="M7.5 6.5 L14 10 L7.5 13.5Z" fill="currentColor"/></svg><span>A face-to-face interview and skills assessment has been undertaken</span></li>
        <li class="blue"><svg class="bullet" viewBox="0 0 20 20"><circle cx="10" cy="10" r="8.5" fill="none" stroke="currentColor" stroke-width="2"/><path d="M7.5 6.5 L14 10 L7.5 13.5Z" fill="currentColor"/></svg><span>Full employment history has been submitted</span></li>
        <li class="teal"><svg class="bullet" viewBox="0 0 20 20"><circle cx="10" cy="10" r="8.5" fill="none" stroke="currentColor" stroke-width="2"/><path d="M7.5 6.5 L14 10 L7.5 13.5Z" fill="currentColor"/></svg><span>Right to work has been recorded and verified</span></li>
        <li class="teal"><svg class="bullet" viewBox="0 0 20 20"><circle cx="10" cy="10" r="8.5" fill="none" stroke="currentColor" stroke-width="2"/><path d="M7.5 6.5 L14 10 L7.5 13.5Z" fill="currentColor"/></svg><span>Fitness to work has been declared</span></li>
        <li class="blue"><svg class="bullet" viewBox="0 0 20 20"><circle cx="10" cy="10" r="8.5" fill="none" stroke="currentColor" stroke-width="2"/><path d="M7.5 6.5 L14 10 L7.5 13.5Z" fill="currentColor"/></svg><span>Two work related references have been obtained and verified</span></li>
        <li class="teal"><svg class="bullet" viewBox="0 0 20 20"><circle cx="10" cy="10" r="8.5" fill="none" stroke="currentColor" stroke-width="2"/><path d="M7.5 6.5 L14 10 L7.5 13.5Z" fill="currentColor"/></svg><span>An enhanced DBS Certificate has been provided</span></li>
        <li class="teal small"><svg class="bullet" viewBox="0 0 20 20"><circle cx="10" cy="10" r="8.5" fill="none" stroke="currentColor" stroke-width="2"/><path d="M7.5 6.5 L14 10 L7.5 13.5Z" fill="currentColor"/></svg><span>In date, sufficient training certificates have been provided and verified or in house training courses have been attended and certificates have been issued.</span></li>
      </ul>
    </div>
  </section>

  <section class="panel panel-training">
    <svg class="panel-art" viewBox="0 0 380 820" preserveAspectRatio="none" aria-hidden="true">
      <defs>
        <linearGradient id="trainingTop" x1="0" y1="0" x2="1" y2="0">
          <stop offset="0" stop-color="#1d55b0"/><stop offset="1" stop-color="#1a47a0"/>
        </linearGradient>
        <linearGradient id="trainingFoot" x1="0" y1="0" x2="1" y2="0">
          <stop offset="0" stop-color="#1a9d8e"/><stop offset="1" stop-color="#17b08c"/>
        </linearGradient>
      </defs>
      <rect x="0" y="0" width="380" height="80" fill="url(#trainingTop)"/>
      <rect x="0" y="735" width="380" height="85" fill="url(#trainingFoot)"/>
    </svg>
    <div class="panel-content">
      <ul class="checks-list">
        <li class="teal"><svg class="bullet" viewBox="0 0 20 20"><circle cx="10" cy="10" r="8.5" fill="none" stroke="currentColor" stroke-width="2"/><path d="M7.5 6.5 L14 10 L7.5 13.5Z" fill="currentColor"/></svg><span>Registration with the appropriate bodies has been verified for Registered Nurses.</span></li>
        <li class="blue"><svg class="bullet" viewBox="0 0 20 20"><circle cx="10" cy="10" r="8.5" fill="none" stroke="currentColor" stroke-width="2"/><path d="M7.5 6.5 L14 10 L7.5 13.5Z" fill="currentColor"/></svg><span>A shadow shift has been completed if it is a brand new staff member</span></li>
        <li class="teal"><svg class="bullet" viewBox="0 0 20 20"><circle cx="10" cy="10" r="8.5" fill="none" stroke="currentColor" stroke-width="2"/><path d="M7.5 6.5 L14 10 L7.5 13.5Z" fill="currentColor"/></svg><span>An ID Badge, uniform, and timesheets have been issued</span></li>
      </ul>
      <div class="training-copy">
        <p>We understand that it is imperative for our clients to only have extremely competent, fully trained staff supporting their existing team. We are proud to cover the standards set within the Care Certificate in the training modules that we deliver to our staff.</p>
        <p>All training is refreshed on an annual basis and we ensure that up to date certificates are held by all staff at all times.</p>
      </div>
    </div>
  </section>

</main>
</body>
</html>
```